Glenmoor Vale Executive Development Workshop Series

* Had error in first version of MS Word doc and have re-uploaded - twelve subject areas, not nine *
I'd like a flyer to print to hand out and post on my website glenmoorvale.com to advertise a workshop series I'm launching. I'd like it to build strongly on the wonderful logo you did and Scottish theme...and to have the same "feel" as my website. glenmoorvale.com
It should be 8.5x11, single sided. Not sure if I should use full color glossy or two-color on nice paper. Regardless, I will most likely have it done on a color copier and will not put it on a printing press.
I have typed up a document with all the information in a MS Word file, but need you to lay it out in an aesthetically pleasing way. I have attached that MS Word file.
I am also attaching a handful of similar flyer documents from other non-competing coaches in my network. I think they all have their merits, but leave me under-whelmed.
I'm also attaching a picture of me and some pictures of Scotland my parents took about 10 years ago. I'm reluctantly open to stock photos, just not too obvious or hackneyed (if that word can be applied to pictures as well as expressions).
Lastly, this workshop series will be an ongoing thing, so I'd like to be able to make minor edits myself with things like new dates or topics.
Thank you!
Target Market(s)
Small business owners and emerging leaders with large companies
Colors
Designer to choose colors to be used in the design.
Requirements
Should not have
- Obviously stock photos

```html
<!DOCTYPE html>
<html lang="en">
<head>
<meta charset="utf-8">
<title>Glenmoor Vale Executive Development Workshop Series</title>
<link rel="stylesheet" href="https://fonts.googleapis.com/css2?family=Tinos:ital,wght@0,400;0,700;1,400&display=swap">
<style>
:root{
  --backdrop:#1e1e1e;
  --paper:#ffffff;
  --forest:#34441c;
  --ink:#2b3614;
  --sage:#b9cf95;
  --mist:#e9e9e7;
  --photo-stone:#8a7f70;
  --photo-red:#b3261e;
  --photo-grass:#6f8a45;
  --photo-hill:#8c9aa3;
  --photo-skin:#c9a48a;
}
*{box-sizing:border-box;margin:0;padding:0}
html,body{width:900px;height:1200px;overflow:hidden;background:var(--backdrop)}
body{font-family:"Tinos","Times New Roman",serif;color:var(--ink)}
.flyer{position:absolute;left:85px;top:127px;width:730px;height:945px;background:var(--paper);overflow:hidden}
.abs{position:absolute}
.brand{left:70px;top:40px;width:260px;display:flex;align-items:center;gap:12px}
.brand-dot{width:22px;height:22px;border-radius:50%;background:var(--forest);flex:none}
.brand-name{font-size:34px;font-weight:400;color:var(--forest);letter-spacing:.5px;line-height:1}
.brand-sub{left:108px;top:86px;font-size:9px;letter-spacing:2.5px;color:var(--forest);border-top:1px solid var(--forest);border-bottom:1px solid var(--forest);padding:2px 8px}
.series-title{left:22px;top:155px;width:390px;font-size:16.5px;font-weight:700;line-height:1.12;color:var(--forest)}
.series-intro{left:22px;top:200px;width:392px;font-size:11.6px;line-height:1.2}
.series-intro .line{display:block;text-align:justify;text-align-last:justify;white-space:nowrap}
.series-intro .line.last{text-align-last:left}
.photo{background:var(--photo-stone)}
.photo-street{left:418px;top:0;width:312px;height:300px;background:linear-gradient(180deg,#9b907f 0%,#857a6a 35%,var(--photo-red) 36%,#9f231b 85%,#a9a49c 86%)}
.photo-cattle{left:0;top:305px;width:215px;height:131px;background:linear-gradient(180deg,#c9d3d6 0%,#7c9352 30%,#8b5a32 55%,#6f8a45 80%)}
.photo-village{left:217px;top:305px;width:201px;height:131px;background:linear-gradient(180deg,#c6d0d8 0%,var(--photo-hill) 22%,#cfcac0 40%,#6f8a45 65%,#8a5a33 100%)}
.topics-banner{left:418px;top:300px;width:312px;height:118px;background:var(--forest);color:#fff;padding:14px 6px 0 7px}
.topics-banner p{font-size:13.6px;font-weight:700;line-height:1.2;white-space:nowrap}
.topics-banner .tagline{font-size:17.5px;margin-top:9px;text-align:center}
.topic{position:absolute;right:0;height:38px}
.topic-bar{position:absolute;top:4px;right:0;height:34px;background:var(--mist);clip-path:polygon(10px 0,100% 0,100% 100%,0 100%)}
.topic-date{position:absolute;top:0;width:44px;height:36px;background:var(--sage);clip-path:polygon(6px 0,100% 0,94% 100%,0 100%);text-align:center;font-weight:700;font-size:12.5px;line-height:13px;padding-top:4px;color:var(--forest)}
.topic-title{position:absolute;top:3px;font-weight:700;font-size:13px;color:var(--ink);white-space:nowrap}
.topic-title small{font-size:9.8px}
.topic-desc{position:absolute;top:19px;font-weight:700;font-size:9.8px;line-height:1.1;color:var(--ink)}
.includes-title{left:16px;top:450px;width:380px;font-size:20.5px;font-weight:700;line-height:1.05;color:var(--forest)}
.list{left:16px;width:352px;list-style:none;font-size:10.4px;line-height:1.18}
.list li{position:relative;padding-left:14px;margin-bottom:9px}
.list li::before{content:"➢";position:absolute;left:0;top:0;font-size:9px}
.list b{font-weight:700}
.register{left:14px;top:652px;width:334px;height:44px;background:var(--forest);color:#fff;clip-path:polygon(0 0,100% 0,96% 100%,0 100%);padding:5px 0 0 8px;font-size:13.5px;line-height:1.2}
.register span{display:block;white-space:nowrap}
.register b{font-size:16.5px}
.portrait{left:22px;top:818px;width:108px;height:110px;background:linear-gradient(180deg,#9fa3a6 0%,var(--photo-skin) 45%,#6b5a48 100%)}
.contact{left:152px;width:200px;display:flex;align-items:center;gap:10px;font-weight:700;color:var(--ink)}
.contact svg{flex:none}
</style>
</head>
<body>
<main class="flyer">
  <div class="abs brand"><span class="brand-dot"></span><span class="brand-name">Glenmoor Vale</span></div>
  <div class="abs brand-sub">BUSINESS COACHING</div>

  <h1 class="abs series-title">GLENMOOR VALE EXECUTIVE DEVELOPMENT WORKSHOP SERIES – FIRST THURSDAYS</h1>
  <p class="abs series-intro">
    <span class="line">A Positive, Fresh, Results-driven Approach For Businesses To Increase Profits By</span>
    <span class="line">Building Confidence, Command And Control In Owners And Executives. We</span>
    <span class="line">Will Use Proven Leadership And Business Strategies To Improve Work-life</span>
    <span class="line">Balance, Buy-in, And Company Value. Here's Your Opportunity To Meet With</span>
    <span class="line">Other Like-minded Business Owners And Executives Once A Month In A Private</span>
    <span class="line last">And Confidential Setting.</span>
  </p>

  <div class="abs photo photo-street" role="img" aria-label="Red-fronted pub on a stone street with a dog statue on a pedestal"></div>
  <div class="abs photo photo-cattle" role="img" aria-label="Highland cow resting on a grassy hillside"></div>
  <div class="abs photo photo-village" role="img" aria-label="Highland cattle grazing above a Scottish village by the water"></div>

  <div class="abs topics-banner">
    <p>We've Got Nine Subject Areas Planned, And<br>While They Are All Powerful, We Will Shift<br>From High-level Strategy Topics To</p>
    <p class="tagline">“where The Rubber Meets The Road”</p>
  </div>

  <section class="schedule">
    <div class="topic" style="top:410px;left:402px"><div class="topic-bar" style="left:40px"></div><div class="topic-date" style="left:0">SEP<br>7</div><div class="topic-title" style="left:55px">MY COMPANY OWNS ME -</div><div class="topic-desc" style="left:55px">what a ceo should and should not do</div></div>
    <div class="topic" style="top:455px;left:396px"><div class="topic-bar" style="left:40px"></div><div class="topic-date" style="left:0">OCT<br>5</div><div class="topic-title" style="left:54px;font-size:10.5px;top:5px">Taking vision / mission / values down to the molecular</div><div class="topic-desc" style="left:54px;top:18px">level of your company</div></div>
    <div class="topic" style="top:500px;left:390px"><div class="topic-bar" style="left:40px"></div><div class="topic-date" style="left:0">NOV<br>2</div><div class="topic-title" style="left:53px">PEOPLE PROBLEMS –</div><div class="topic-desc" style="left:51px">the biggest waste of time and money for every small business</div></div>
    <div class="topic" style="top:545px;left:384px"><div class="topic-bar" style="left:40px"></div><div class="topic-date" style="left:0">DEC<br>7</div><div class="topic-title" style="left:53px">VALUE DELIVERY SYSTEMS -</div><div class="topic-desc" style="left:50px">re-think everything you think you know about creating value</div></div>
    <div class="topic" style="top:590px;left:378px"><div class="topic-bar" style="left:40px"></div><div class="topic-date" style="left:0">JAN<br>4</div><div class="topic-title" style="left:53px">RALLY YOUR TEAM AROUND A GOAL</div><div class="topic-desc" style="left:51px;width:250px">how to create a meaningful company goal and rally the troops around it</div></div>
    <div class="topic" style="top:634px;left:372px"><div class="topic-bar" style="left:40px"></div><div class="topic-date" style="left:0">FEB<br>1</div><div class="topic-title" style="left:50px">BUILDING YOUR EXECUTIVE</div><div class="topic-title" style="left:50px;top:18px">LEADERSHIP TEAM <small>– you can't succeed without one</small></div></div>
    <div class="topic" style="top:679px;left:366px"><div class="topic-bar" style="left:40px"></div><div class="topic-date" style="left:0">MAR<br>1</div><div class="topic-title" style="left:50px">IMPROVE YOUR OUTSIDE SALES EFFORTS -</div><div class="topic-desc" style="left:49px">help your sales force to be busy and successful</div></div>
    <div class="topic" style="top:724px;left:360px"><div class="topic-bar" style="left:40px"></div><div class="topic-date" style="left:0">APR<br>5</div><div class="topic-title" style="left:48px">EVERY BRAIN IN THE GAME -</div><div class="topic-desc" style="left:48px">engage your team and build a strong culture</div></div>
    <div class="topic" style="top:769px;left:354px"><div class="topic-bar" style="left:40px"></div><div class="topic-date" style="left:0">MAY<br>3</div><div class="topic-title" style="left:47px">REPEATABLE PROCESSES -</div><div class="topic-desc" style="left:46px">coach your employees how to get predictable results every time</div></div>
    <div class="topic" style="top:814px;left:348px"><div class="topic-bar" style="left:40px"></div><div class="topic-date" style="left:0">JUN<br>7</div><div class="topic-title" style="left:47px">FINDING AND FILLING PROFIT HOLES -</div><div class="topic-desc" style="left:46px">most small businesses waste more money than they profit</div></div>
    <div class="topic" style="top:859px;left:342px"><div class="topic-bar" style="left:40px"></div><div class="topic-date" style="left:0">*JUL<br>12</div><div class="topic-title" style="left:46px">PUT YOUR PAYROLL ON A DIET -</div><div class="topic-desc" style="left:44px">why waste happens, what to do about it and how it helps everyone</div></div>
    <div class="topic" style="top:904px;left:336px"><div class="topic-bar" style="left:40px"></div><div class="topic-date" style="left:0">AUG<br>2</div><div class="topic-title" style="left:46px">TRULY,-</div><div class="topic-desc" style="left:44px">how effective are you with this whole “leadership” thing?</div></div>
  </section>

  <h2 class="abs includes-title">EACH MONTH OF THIS MONTHLY WORKSHOP SERIES INCLUDES:</h2>
  <ul class="abs list" style="top:502px">
    <li><b>3-HOUR INTENSIVE WORKSHOP</b> - high-energy, creative sessions with engaging and relevant business topics, peer group advisory board (master mind), and networking (9am – 12pm, dates above)</li>
    <li><b>90-MINUTE ONE-ON-ONE COACHING SESSION</b> – to help you absorb and apply the revelations from the group sessions to your own business (mutually scheduled)</li>
    <li>Participation and trust is vital to your investment; no holding back. Due to the confidential nature of the intensive workshops, all participants will sign a confidentiality agreement. Additionally, we will only allow one company per industry to be represented.</li>
  </ul>

  <div class="abs register"><span>To register, go to <b>glenmoorvale.com/exec-dev</b> and</span><span>click the registration link</span></div>

  <ul class="abs list" style="top:712px;width:315px">
    <li>$395/month or $295/month with a 6-month or greater commitment</li>
    <li>All monthly Intensive Workshops will be 9am – 12pm on the dates above at Foundry Coworking at 218 Harbor Lane, Millbrook NC 27000</li>
    <li>All one-on-one coaching sessions will be mutually scheduled with Ewan Baird once you have registered</li>
  </ul>

  <div class="abs portrait" role="img" aria-label="Portrait of coach Ewan Baird"></div>

  <div class="abs contact" style="top:820px;font-size:11px;line-height:1.2">
    <svg width="20" height="20" viewBox="0 0 20 20"><circle cx="10" cy="10" r="9" fill="none" stroke="#2b3614" stroke-width="1.6"/><path d="M10 4.5a3.5 3.5 0 0 0-3.5 3.5c0 2.6 3.5 7 3.5 7s3.5-4.4 3.5-7A3.5 3.5 0 0 0 10 4.5z" fill="#2b3614"/><circle cx="10" cy="8" r="1.3" fill="#fff"/></svg>
    <span>218 harbor lane<br>millbrook, nc 27000</span>
  </div>
  <div class="abs contact" style="top:853px;font-size:16px">
    <svg width="20" height="20" viewBox="0 0 20 20"><circle cx="10" cy="10" r="9" fill="none" stroke="#2b3614" stroke-width="1.6"/><path d="M7 5l2 2.5-1.2 1.3a7 7 0 0 0 3.4 3.4L12.5 11 15 13l-1.3 1.5C10 14.5 5.5 10 5.5 6.3z" fill="#2b3614"/></svg>
    <span>(555) 014-2290</span>
  </div>
  <div class="abs contact" style="top:880px;font-size:12px">
    <svg width="20" height="20" viewBox="0 0 20 20"><circle cx="10" cy="10" r="9.5" fill="#2b3614"/><rect x="5" y="6.5" width="10" height="7" fill="#fff"/><path d="M5 6.5l5 4 5-4" fill="none" stroke="#2b3614" stroke-width="1"/></svg>
    <span>ewan@glenmoorvale.com</span>
  </div>
  <div class="abs contact" style="top:905px;font-size:12px">
    <svg width="20" height="20" viewBox="0 0 20 20"><circle cx="10" cy="10" r="9.5" fill="#2b3614"/><g fill="none" stroke="#fff" stroke-width="1"><circle cx="10" cy="10" r="6"/><ellipse cx="10" cy="10" rx="2.6" ry="6"/><path d="M4 10h12M5 7h10M5 13h10"/></g></svg>
    <span>http://glenmoorvale.com/</span>
  </div>
</main>
</body>
</html>
```